Bolstering Marveno Inc needs a business card design

Looking for a unique, classy and sharp business card design.

Contact Information for Business Card

Bolstering Marveno Inc.
Lidia Osorno Bermudez BScOT(c)
Occupational Therapist
(780) 555-0142
bolsteringmarveno@mailvora.com

```html
<!DOCTYPE html>
<html lang="en">
<head>
<meta charset="utf-8">
<title>Bolstering Marveno Inc. – Business Card</title>
<link href="https://fonts.googleapis.com/css2?family=Ubuntu:wght@500;700&display=swap" rel="stylesheet">
<style>
  :root {
    --lime: #8cc63f;
    --lime-faint: #e3efd2;
    --purple: #8a1e8c;
    --white: #ffffff;
    --stage: #e9e9e7;
    --shadow: rgba(0, 0, 0, 0.18);
  }
  html, body {
    margin: 0;
    padding: 0;
    overflow: hidden;
  }
  .canvas {
    width: 1200px;
    height: 800px;
    background: var(--stage);
    position: relative;
    overflow: hidden;
    font-family: "Ubuntu", sans-serif;
  }
  .card {
    position: absolute;
    top: 245px;
    width: 540px;
    height: 309px;
    box-shadow: 0 8px 24px var(--shadow);
    overflow: hidden;
  }
  .card--front {
    left: 40px;
    background: var(--white);
  }
  .card--back {
    left: 620px;
    background: var(--lime);
    display: flex;
    align-items: center;
    justify-content: center;
  }
  .front-band {
    position: absolute;
    left: 22px;
    top: 0;
    width: 62px;
    height: 100%;
    background: var(--lime);
  }
  .front-mark {
    position: absolute;
    right: -40px;
    top: 90px;
    width: 260px;
    height: 260px;
    border-radius: 50%;
    background: var(--lime-faint);
  }
  .front-content {
    position: absolute;
    left: 112px;
    top: 40px;
  }
  .brand {
    display: flex;
    align-items: center;
    gap: 10px;
    margin-bottom: 42px;
  }
  .brand__dot {
    width: 18px;
    height: 18px;
    border-radius: 50%;
    background: var(--lime);
  }
  .brand__name {
    font-weight: 700;
    font-size: 26px;
    color: var(--purple);
    letter-spacing: -0.3px;
  }
  .person__name {
    font-weight: 500;
    font-size: 19px;
    color: var(--lime);
    margin: 0 0 4px;
  }
  .person__role {
    font-weight: 700;
    font-size: 16px;
    color: var(--purple);
    margin: 0 0 16px;
  }
  .contact {
    list-style: none;
    margin: 0;
    padding: 0;
    color: var(--purple);
    font-weight: 500;
    font-size: 16px;
  }
  .contact li {
    display: flex;
    align-items: center;
    gap: 8px;
    margin-bottom: 6px;
  }
  .contact svg {
    width: 15px;
    height: 15px;
    fill: var(--purple);
    flex: none;
  }
  .back-name {
    font-weight: 700;
    font-size: 34px;
    color: var(--purple);
    letter-spacing: -0.4px;
  }
</style>
</head>
<body>
<div class="canvas">
  <section class="card card--front">
    <div class="front-band"></div>
    <div class="front-mark"></div>
    <div class="front-content">
      <div class="brand">
        <span class="brand__dot"></span>
        <span class="brand__name">Bolstering Marveno Inc.</span>
      </div>
      <p class="person__name">Lidia Osorno Bermudez BScOT(c)</p>
      <p class="person__role">Occupational Therapist</p>
      <ul class="contact">
        <li>
          <svg viewBox="0 0 24 24" aria-hidden="true"><path d="M6.6 10.8a15.1 15.1 0 0 0 6.6 6.6l2.2-2.2c.3-.3.7-.4 1-.2 1.1.4 2.3.6 3.6.6.6 0 1 .4 1 1V20c0 .6-.4 1-1 1A17 17 0 0 1 3 4c0-.6.4-1 1-1h3.5c.6 0 1 .4 1 1 0 1.3.2 2.5.6 3.6.1.3 0 .7-.2 1z"/></svg>
          (780) 555-0142
        </li>
        <li>
          <svg viewBox="0 0 24 24" aria-hidden="true"><path d="M2 5h20v14H2z M2 5l10 7 10-7" fill="none" stroke="#8a1e8c" stroke-width="2"/><path d="M2 5h20l-10 7z"/></svg>
          bolsteringmarveno@mailvora.com
        </li>
      </ul>
    </div>
  </section>

  <section class="card card--back">
    <span class="back-name">Bolstering Marveno Inc.</span>
  </section>
</div>
</body>
</html>
```